Membership Drive "CHRISTMAS SPECIAL"

Looking to run a "Christmas Special" on 6 month Memberships for December 2019 to boost membership number up. This is a great time to get people exercising and everyone loves a Christmas Sale. Special is designed to attract more people to join and enjoy the savings.
Artwork will be display via social media (PX and Pictoria) as well as in store. Artwork must be eye catching and direct to the customer. Customer should feel a sense of relief with being able to exercise at a lower cost .

Heading: "Christmas Sale"
6 Months
$199.00 Save over 30%
Terms and conditions apply"
*Offer End 31st December

below are other promos we had designed on Sketch Harbor along with potential photos to be included into this promo

Target Market(s)

Males and Females aged between 16 - 45

Industry/Entity Type

Fitness

Colors

Designer to choose colors to be used in the design.

Requirements
Must have
• Must emphasize "Christmas Special" $199.00 Save over 30%
• Terms and conditions apply
• Offer Ends 31st of December
• "All of our contact details"
• Address: 14 Wattle Rd Greenfield Park 3051
• Ph: 9482 6107
• www.summitfitclub.com.au
• Design format must come in PDF for a AO poster and an Pictoria format please
Nice to have
• Some Christmas feels to the artwork

```html
<!DOCTYPE html>
<html lang="en">
<head>
<meta charset="utf-8">
<title>Christmas Sale – Summit Fit Club</title>
<link rel="stylesheet" href="https://fonts.googleapis.com/css2?family=Great+Vibes&family=Montserrat:wght@800&family=Open+Sans:ital,wght@0,300;0,400;1,700;1,800&display=swap">
<style>
  :root {
    --red-deep: #98000f;
    --red-main: #ad0010;
    --red-bright: #ec2a32;
    --red-glow: #d9141f;
    --gold: #fcc20c;
    --gold-light: #ffd84a;
    --gold-dark: #e8a400;
    --white: #ffffff;
    --ink: #1a1a1a;
  }
  * { margin: 0; padding: 0; box-sizing: border-box; }
  html, body { width: 1200px; height: 600px; overflow: hidden; background: var(--red-main); }
  .poster {
    position: relative;
    width: 1200px;
    height: 600px;
    overflow: hidden;
    background: linear-gradient(90deg, var(--red-deep) 0%, var(--red-main) 50%, #a5000e 100%);
    font-family: "Open Sans", sans-serif;
    color: var(--white);
  }
  .snowflake-art {
    position: absolute;
    left: 0; top: 0;
    width: 720px; height: 600px;
    background:
      radial-gradient(circle at 130px 170px, rgba(240,40,48,.95) 0, rgba(222,24,34,.7) 70px, rgba(222,24,34,0) 150px),
      radial-gradient(circle at 470px 110px, rgba(240,40,48,.9) 0, rgba(222,24,34,.65) 60px, rgba(222,24,34,0) 135px),
      radial-gradient(circle at 310px 400px, rgba(232,34,42,.8) 0, rgba(214,20,30,.55) 70px, rgba(214,20,30,0) 150px),
      radial-gradient(circle at 540px 480px, rgba(240,40,48,.9) 0, rgba(222,24,34,.6) 55px, rgba(222,24,34,0) 120px),
      radial-gradient(circle at 150px 560px, rgba(236,36,44,.85) 0, rgba(222,24,34,.55) 55px, rgba(222,24,34,0) 120px),
      radial-gradient(circle at 30px 420px, rgba(232,34,42,.7) 0, rgba(222,24,34,0) 80px),
      radial-gradient(circle at 290px 20px, rgba(236,36,44,.85) 0, rgba(222,24,34,0) 45px),
      radial-gradient(circle at 480px 310px, rgba(236,36,44,.85) 0, rgba(222,24,34,0) 50px),
      radial-gradient(circle at 130px 410px, rgba(236,36,44,.85) 0, rgba(222,24,34,0) 45px),
      radial-gradient(circle at 380px 560px, rgba(236,36,44,.85) 0, rgba(222,24,34,0) 45px),
      radial-gradient(circle at 320px 180px, rgba(255,120,120,.35) 0, rgba(255,120,120,0) 25px),
      radial-gradient(circle at 430px 75px, rgba(255,140,140,.4) 0, rgba(255,140,140,0) 20px),
      radial-gradient(circle at 540px 510px, rgba(255,140,140,.35) 0, rgba(255,140,140,0) 22px);
  }
  .heading {
    position: absolute;
    left: 626px; top: 38px;
    font-family: "Great Vibes", cursive;
    font-size: 150px;
    line-height: 1;
    font-weight: 400;
    color: var(--white);
  }
  .sale-badge {
    position: absolute;
    left: 570px; top: 170px;
    width: 480px; height: 130px;
  }
  .sale-word {
    position: absolute;
    left: 712px; top: 216px;
    font-family: "Montserrat", sans-serif;
    font-weight: 800;
    font-size: 56px;
    line-height: 1;
    letter-spacing: 3px;
    color: var(--ink);
  }
  .term {
    position: absolute;
    left: 968px; top: 246px;
    font-weight: 800;
    font-style: italic;
    font-size: 25px;
    color: var(--white);
  }
  .price-line {
    position: absolute;
    left: 544px; top: 312px;
    font-weight: 800;
    font-style: italic;
    color: var(--gold);
    white-space: nowrap;
    line-height: 1;
  }
  .price-line .price { font-size: 52px; }
  .price-line .save { font-size: 68px; margin-left: 14px; }
  .price-line .saving { font-size: 50px; margin-left: 14px; }
  .contact {
    position: absolute;
    left: 690px; top: 424px;
    width: 400px;
    text-align: center;
    font-weight: 700;
    font-style: italic;
    font-size: 17px;
    line-height: 23px;
    text-transform: uppercase;
  }
  .fine-print {
    position: absolute;
    right: 28px; top: 544px;
    font-weight: 300;
    font-size: 17px;
    white-space: nowrap;
  }
  .fine-print .divider { margin: 0 12px; }
</style>
</head>
<body>
  <main class="poster">
    <div class="snowflake-art" role="img" aria-label="Red glitter snowflakes and red stars scattered with sparkles"></div>

    <h1 class="heading">Christmas</h1>

    <svg class="sale-badge" viewBox="570 170 480 130" aria-hidden="true">
      <line x1="578" y1="196" x2="632" y2="220" stroke="var(--white)" stroke-width="3"/>
      <line x1="572" y1="224" x2="634" y2="234" stroke="var(--gold)" stroke-width="3"/>
      <line x1="590" y1="246" x2="640" y2="246" stroke="var(--white)" stroke-width="2"/>
      <polygon points="650,228 968,196 954,284 672,286" fill="var(--white)"/>
      <polygon points="658,232 960,202 948,278 678,280" fill="var(--gold)"/>
      <polygon points="658,232 960,202 955,226 664,252" fill="var(--gold-light)"/>
      <line x1="985" y1="196" x2="1040" y2="176" stroke="var(--gold)" stroke-width="3"/>
      <line x1="990" y1="213" x2="1046" y2="204" stroke="var(--white)" stroke-width="2"/>
      <line x1="976" y1="186" x2="1010" y2="172" stroke="var(--gold-dark)" stroke-width="2"/>
    </svg>
    <div class="sale-word">SALE</div>
    <div class="term">6 Months</div>

    <p class="price-line">
      <span class="price">$199.00</span><span class="save">SAVE</span><span class="saving">over 30%</span>
    </p>

    <address class="contact">
      Address: 14 Wattle Rd Greenfield Park 3051<br>
      Ph: 9482 6107<br>
      www.summitfitclub.com.au
    </address>

    <p class="fine-print">Terms and conditions apply"<span class="divider">|</span>*Offer End 31st December</p>
  </main>
</body>
</html>
```